Brindle painting & waterproofing business card.

Business cards updated to reflect photos attached. we have given the photos of the old business cards and some of our updated designs for other items we have here in the office. Please see attached. if anyone needs to contact us directly for clarification you can email us at brindlerestoration@mailcove.example

Industry/Entity Type

Construction

Contact Information for Business Card

See attached photos

Font styles to use
Other font styles liked:
• Same as photos

Colors
ec1f27

Requirements
Must have
• Employee Names,
• Dennis Marlow II, Supervisor/Owner
• Dee Marlow, President/Owner
• Gus Tremby, Sales Representative
• Lyle Varsen, Supervisor
• Change 20 years to 25
Nice to have
• ideas reflecting the attached photos
Should not have
• should not be exactly like attached photos as those are old business card but reflect to match new logo listed as korvel van and cup photo.

```html
<!DOCTYPE html>
<html lang="en">
<head>
<meta charset="utf-8">
<title>Brindle's Business Card</title>
<link rel="stylesheet" href="https://fonts.googleapis.com/css2?family=Roboto:wght@400;700&display=swap">
<style>
  :root {
    --brand-red: #ec1f27;
    --card-white: #ffffff;
    --ink: #222222;
    --rule: #1a1a1a;
    --backdrop: #1c1c1c;
  }
  * { box-sizing: border-box; margin: 0; padding: 0; }
  html, body { width: 1200px; height: 862px; overflow: hidden; }
  body {
    background: var(--backdrop);
    display: flex;
    align-items: center;
    justify-content: center;
    gap: 40px;
    font-family: "Roboto", Arial, sans-serif;
  }
  .card {
    width: 560px;
    height: 320px;
    border-radius: 22px;
    position: relative;
    overflow: hidden;
  }
  .card-front {
    background: var(--brand-red);
    display: flex;
    align-items: center;
    justify-content: center;
  }
  .brand {
    display: flex;
    align-items: center;
    gap: 12px;
    font-family: "Roboto", Arial, sans-serif;
    font-weight: 700;
    line-height: 1;
  }
  .brand-mark { display: block; flex: none; }
  .card-front .brand { color: var(--card-white); font-size: 58px; }
  .card-front .brand-mark { width: 22px; height: 22px; background: var(--card-white); }
  .card-back { background: var(--card-white); color: var(--ink); }
  .card-back .brand {
    position: absolute;
    left: 36px;
    top: 34px;
    color: var(--brand-red);
    font-size: 36px;
    gap: 9px;
  }
  .card-back .brand-mark { width: 14px; height: 14px; background: var(--brand-red); }
  .person {
    position: absolute;
    right: 34px;
    top: 112px;
    text-align: right;
  }
  .person-name {
    color: var(--brand-red);
    font-weight: 700;
    font-size: 25px;
    line-height: 1.1;
  }
  .person-title { font-size: 14px; margin-top: 5px; }
  .divider {
    position: absolute;
    left: 80px;
    right: 150px;
    top: 182px;
    border-top: 1.5px solid var(--rule);
  }
  .address {
    position: absolute;
    right: 34px;
    top: 198px;
    text-align: right;
    font-size: 12.5px;
    line-height: 1.45;
    text-transform: uppercase;
  }
  .address-line { display: flex; align-items: center; justify-content: flex-end; gap: 6px; }
  .contact-list {
    position: absolute;
    left: 80px;
    bottom: 30px;
    list-style: none;
    font-size: 14px;
    line-height: 1.55;
  }
  .contact-list li { display: flex; align-items: center; gap: 8px; }
  .icon { width: 12px; height: 12px; fill: var(--brand-red); flex: none; }
</style>
</head>
<body>
  <section class="card card-front">
    <div class="brand"><span class="brand-mark"></span>Brindle's</div>
  </section>

  <section class="card card-back">
    <div class="brand"><span class="brand-mark"></span>Brindle's</div>

    <div class="person">
      <div class="person-name">Dennis Marlow II</div>
      <div class="person-title">Supervisor/Owner</div>
    </div>

    <div class="divider"></div>

    <div class="address">
      <div class="address-line">480 Harbor Ridge Rd
        <svg class="icon" viewBox="0 0 12 12"><path d="M6 0a4 4 0 0 0-4 4c0 3 4 8 4 8s4-5 4-8a4 4 0 0 0-4-4zm0 5.5A1.5 1.5 0 1 1 6 2.5a1.5 1.5 0 0 1 0 3z"/></svg>
      </div>
      <div class="address-line">Cedar Point, ST 00417</div>
      <div class="address-line">www.brindlerestoration.example</div>
    </div>

    <ul class="contact-list">
      <li><svg class="icon" viewBox="0 0 12 12"><path d="M2.5 0.5l2 2.5-1 1.3a7 7 0 0 0 4.2 4.2l1.3-1 2.5 2-1.2 1.8C5.5 11 1 6.5 0.7 1.7z"/></svg>555.214.7380</li>
      <li><svg class="icon" viewBox="0 0 12 12"><path d="M0 2h12v8H0zM1 3v.4l5 3.3 5-3.3V3z"/></svg>555.309.6142</li>
      <li><svg class="icon" viewBox="0 0 12 12"><circle cx="6" cy="6" r="6"/></svg>brindlerestoration@mailcove.example</li>
    </ul>
  </section>
</body>
</html>
```